Lumen Path - Fiber Internet to the home postcard

Design a postcard for my company, Lumen Path, using the logo below. On the front of the card:
- No Buffering • No BS
- Second line should be the logo
- $60 / month • 10-Gigs
- lumenpath.net

Color palate should follow the colors in the logo.

Address should say
- Special pricing during construction
- Our best price
- Our fastest speed
- $60 / month • 10-Gigs
- lumenpath.net

Target Market(s)

25 - 55 year olds. Middle income/class. People with kids and pick up trucks

Industry/Entity Type

Fiber Internet Service Provider

Font styles to use
Sans Serif

Colors

Designer to choose colors to be used in the design.

Requirements
Nice to have
• I am open to more creative changes

```html
<!DOCTYPE html>
<html lang="en">
<head>
<meta charset="utf-8">
<title>Lumen Path – Fiber Postcard</title>
<link rel="stylesheet" href="https://fonts.googleapis.com/css2?family=Exo+2:ital,wght@1,800;1,900&family=Montserrat:wght@500;700;800&display=swap">
<style>
  :root{
    --navy:#002a5c;
    --navy-deep:#03102a;
    --green:#7ac143;
    --sky:#dcedfa;
    --sky-light:#f1f8fe;
    --paper:#ffffff;
    --stage:#d6d6d6;
    --stamp:#e6e6e6;
    --rule:#9a9a9a;
  }
  *{box-sizing:border-box;margin:0;padding:0}
  html,body{width:856px;height:1200px;overflow:hidden}
  body{background:var(--stage);position:relative;font-family:"Montserrat",sans-serif}

  .card{position:absolute;left:80px;width:696px;height:497px;overflow:hidden}

  /* Front */
  .card-front{top:80px;background:var(--navy)}
  .front-field{position:absolute;inset:12px;
    background:radial-gradient(ellipse at 50% 45%,var(--sky-light) 0%,var(--sky) 65%,#c9e2f4 100%)}
  .front-art{position:absolute;inset:0}
  .brand-line{position:absolute;left:0;right:0;top:148px;height:150px;
    display:flex;align-items:center;justify-content:center;gap:18px}
  .brand-name{font-family:"Montserrat",sans-serif;font-weight:800;font-size:64px;
    color:var(--navy);letter-spacing:-1px}
  .brand-dot{width:128px;height:128px;border-radius:50%;background:var(--green)}
  .front-url{position:absolute;left:0;right:0;top:432px;text-align:center;
    font-family:"Montserrat",sans-serif;font-weight:700;font-size:26px;
    letter-spacing:5px;color:var(--navy)}

  /* Back */
  .card-back{top:631px;background:var(--paper)}
  .back-art{position:absolute;inset:0}
  .perks{position:absolute;left:45px;top:48px;list-style:none;color:#fff}
  .perks li{display:flex;align-items:flex-start;gap:9px;font-weight:700;
    font-size:23px;line-height:32px;margin-bottom:7px}
  .perks li svg{flex:none;margin-top:6px}
  .about{position:absolute;left:45px;top:335px;color:#fff;font-weight:500;
    font-size:16px;line-height:20.5px;width:210px}
  .about-rule{position:absolute;left:45px;top:402px;width:204px;height:2px;background:#fff}
  .contact{position:absolute;left:45px;color:#fff;font-weight:700;font-size:18px;
    display:flex;align-items:center;gap:7px}
  .contact-phone{top:415px}
  .contact-web{top:444px}
  .back-brand{position:absolute;left:422px;top:73px;display:flex;align-items:center;gap:5px}
  .back-brand .brand-name{font-size:19px;letter-spacing:-0.3px}
  .back-brand .brand-dot{width:24px;height:24px}
  .stamp-box{position:absolute;left:568px;top:44px;width:83px;height:83px;background:var(--stamp)}
  .address-line{position:absolute;left:472px;width:179px;height:1px;background:var(--rule)}
</style>
</head>
<body>

<section class="card card-front">
  <div class="front-field" role="img" aria-label="Soft blue background with a faint network of connected fiber nodes"></div>
  <svg class="front-art" width="696" height="497" viewBox="0 0 696 497">
    <polygon points="75,52 434,52 419,126 57,126" fill="var(--navy)"/>
    <polygon points="434,52 640,52 624,126 419,126" fill="var(--green)"/>
    <text x="97" y="106" font-family="'Exo 2',sans-serif" font-style="italic" font-weight="900" font-size="46" fill="var(--green)" textLength="300" lengthAdjust="spacingAndGlyphs">No Buffering</text>
    <text x="458" y="106" font-family="'Exo 2',sans-serif" font-style="italic" font-weight="900" font-size="44" fill="#fff" textLength="142" lengthAdjust="spacingAndGlyphs">No BS</text>

    <polygon points="75,330 640,330 624,403 57,403" fill="var(--green)"/>
    <polygon points="391,319 621,319 600,413 370,413" fill="var(--navy)"/>
    <text x="99" y="387" font-family="'Exo 2',sans-serif" font-style="italic" font-weight="900" font-size="58" fill="var(--navy)" textLength="105" lengthAdjust="spacingAndGlyphs">$60</text>
    <text x="212" y="384" font-family="'Exo 2',sans-serif" font-style="italic" font-weight="900" font-size="40" fill="var(--navy)" textLength="144" lengthAdjust="spacingAndGlyphs">/month</text>
    <text x="397" y="385" font-family="'Exo 2',sans-serif" font-style="italic" font-weight="900" font-size="50" fill="#fff" textLength="196" lengthAdjust="spacingAndGlyphs">10-Gigs</text>
  </svg>
  <div class="brand-line">
    <span class="brand-name">Lumen Path</span>
    <span class="brand-dot"></span>
  </div>
  <div class="front-url">www.lumenpath.net</div>
</section>

<section class="card card-back">
  <svg class="back-art" width="696" height="497" viewBox="0 0 696 497">
    <defs>
      <radialGradient id="fiberGlow" cx="0.7" cy="0.6" r="0.8">
        <stop offset="0" stop-color="#1d4d8f"/>
        <stop offset="0.55" stop-color="#0a2150"/>
        <stop offset="1" stop-color="var(--navy-deep)"/>
      </radialGradient>
    </defs>
    <circle cx="194" cy="107" r="212" fill="url(#fiberGlow)" role="img" aria-label="Photo of glowing blue fiber optic strands"/>
    <path d="M388 0 A222 222 0 0 1 407 48" fill="none" stroke="var(--green)" stroke-width="1.5"/>
    <path d="M364 257 A227 227 0 0 1 273 326" fill="none" stroke="var(--green)" stroke-width="1.5"/>
    <circle cx="139" cy="471" r="197" fill="var(--green)"/>
    <path d="M0 332 A200 200 0 0 1 335 455" fill="none" stroke="var(--navy)" stroke-width="1.5"/>
  </svg>

  <ul class="perks">
    <li><svg width="23" height="23" viewBox="0 0 24 24"><circle cx="12" cy="12" r="11" fill="var(--green)"/><circle cx="12" cy="12" r="7.5" fill="none" stroke="#fff" stroke-width="1.4"/><path d="M8.5 12.2l2.4 2.4 4.6-4.8" fill="none" stroke="#fff" stroke-width="1.6"/></svg><span>Special pricing<br>during construction</span></li>
    <li><svg width="23" height="23" viewBox="0 0 24 24"><circle cx="12" cy="12" r="11" fill="var(--green)"/><circle cx="12" cy="12" r="7.5" fill="none" stroke="#fff" stroke-width="1.4"/><path d="M8.5 12.2l2.4 2.4 4.6-4.8" fill="none" stroke="#fff" stroke-width="1.6"/></svg><span>Our best price</span></li>
    <li><svg width="23" height="23" viewBox="0 0 24 24"><circle cx="12" cy="12" r="11" fill="var(--green)"/><circle cx="12" cy="12" r="7.5" fill="none" stroke="#fff" stroke-width="1.4"/><path d="M8.5 12.2l2.4 2.4 4.6-4.8" fill="none" stroke="#fff" stroke-width="1.6"/></svg><span>Our fastest speed</span></li>
    <li><svg width="23" height="23" viewBox="0 0 24 24"><circle cx="12" cy="12" r="11" fill="var(--green)"/><circle cx="12" cy="12" r="7.5" fill="none" stroke="#fff" stroke-width="1.4"/><path d="M8.5 12.2l2.4 2.4 4.6-4.8" fill="none" stroke="#fff" stroke-width="1.6"/></svg><span>$60 / month • 10-Gigs</span></li>
  </ul>

  <p class="about">Internet Service Provider to Florida’s Volusia and Brevard Counties</p>
  <div class="about-rule"></div>
  <div class="contact contact-phone">
    <svg width="18" height="18" viewBox="0 0 24 24"><circle cx="12" cy="12" r="10.5" fill="none" stroke="#fff" stroke-width="1.6"/><path d="M8.6 7.2l1.6-.4 1.2 2.6-1 .9c.6 1.4 1.6 2.5 3 3.2l.9-1 2.6 1.2-.4 1.6c-.2.6-.8 1-1.4.9-3.6-.6-6.2-3.2-6.9-6.8-.1-.6.2-1.1.4-1.2z" fill="#fff"/></svg>
    <span>(555) 014-2290</span>
  </div>
  <div class="contact contact-web">
    <svg width="18" height="18" viewBox="0 0 24 24" fill="none" stroke="#fff" stroke-width="1.6"><circle cx="12" cy="12" r="10"/><ellipse cx="12" cy="12" rx="4.5" ry="10"/><path d="M2 12h20M4 7h16M4 17h16"/></svg>
    <span>lumenpath.net</span>
  </div>

  <div class="back-brand">
    <span class="brand-name">Lumen Path</span>
    <span class="brand-dot"></span>
  </div>
  <div class="stamp-box"></div>
  <div class="address-line" style="top:287px"></div>
  <div class="address-line" style="top:328px"></div>
  <div class="address-line" style="top:368px"></div>
</section>

</body>
</html>
```